Heron Freightways LLC needs a web desigh ASAP!

We need a fully functioning web site for our trucking company!
we currently have our domain and logo.
Attached you will find our logo files and word documents with info we would like to include in our web page. (Navigation Tabs and dropdown menu)
Our domain is heronfreightways.net (from webnestly)
Our Chatterbook page is Heron Freightways LLC. You can find pictures and a little bit about our company.
our original logo is the one with bull on the left side.
Our trucking company is based in south Texas, but travel within the USA and Canada.

Target Market(s)

Logistic
Refrigerated Fleet Clients
Transportation
Trucking companies

Industry/Entity Type

Trucking Company

Coding

Coded - Design and coding required

Number of Pages Required

1 page

Font styles to use
Sans Serif

Colors
f04a51
3277b5
ffffff

Requirements
Must have
• our main email contact is Info@heronfreightways.net
• we would like see the colors of our logo. it would be nice to have a truck with our logo in the background.
• We need a web site that we can manage on our own easily.
Nice to have
• roads, highways
• get a quote module
• our inspirational web pages are:
• www.marwickhaulage.com
• www.dorvelcargo.com
• we are open to use stock photos

```html
<!DOCTYPE html>
<html lang="en">
<head>
<meta charset="utf-8">
<title>Heron Freightways LLC</title>
<link href="https://fonts.googleapis.com/css2?family=Roboto:ital,wght@0,300;0,400;0,500;0,700;1,400;1,500&display=swap" rel="stylesheet">
<style>
:root{
  --red:#f04a51;
  --red-dark:#c9252d;
  --blue:#3277b5;
  --white:#ffffff;
  --ink:#333333;
  --charcoal:#2e2e2e;
  --sky:#6fa7de;
  --sand:#c7a77a;
  --truck-yellow:#f2c21b;
}
*{box-sizing:border-box;margin:0;padding:0}
html,body{width:1200px;height:3136px;overflow:hidden}
body{font-family:'Roboto',Arial,sans-serif;color:var(--ink);background:var(--white);position:relative}

/* header */
.site-header{position:absolute;left:0;top:0;width:1200px;height:130px;background:var(--white);box-shadow:0 2px 6px rgba(0,0,0,.08);z-index:2}
.brand{position:absolute;left:96px;top:52px;display:flex;align-items:center;gap:12px;font-weight:700;font-size:30px;color:var(--red);letter-spacing:-.5px}
.brand-dot{width:30px;height:30px;border-radius:50%;background:var(--blue)}
.main-nav{position:absolute;left:476px;top:31px;height:99px;display:flex}
.main-nav a{display:flex;align-items:center;padding:0 17px;font-size:15px;font-weight:500;color:#222;text-decoration:none;text-transform:uppercase}
.main-nav a.active{background:var(--red);color:var(--white);padding:0 20px}

/* hero */
.hero{position:absolute;left:0;top:130px;width:1200px;height:597px;
  background:
    radial-gradient(ellipse 330px 230px at 330px 250px,rgba(242,194,27,.85),rgba(242,194,27,0) 75%),
    radial-gradient(ellipse 520px 170px at 880px 250px,rgba(236,236,236,.9),rgba(236,236,236,0) 80%),
    linear-gradient(180deg,#5b9ad8 0%,#9cc4ea 35%,#d9d4c6 52%,#c7a77a 68%,#9c7a55 100%)}
.hero-arrow{position:absolute;top:173px;width:42px;height:188px;background:rgba(80,80,80,.55);display:flex;align-items:center;justify-content:center}
.hero-arrow.prev{left:88px}
.hero-arrow.next{left:1070px}
.hero-caption{position:absolute;left:276px;top:190px;width:648px;height:165px;background:rgba(0,0,0,.6);border:2px solid rgba(255,255,255,.55);text-align:center;color:var(--white)}
.hero-caption h1{font-size:45px;font-weight:700;line-height:52px;margin-top:16px;text-transform:uppercase}
.hero-caption p{font-size:19px;font-weight:500;letter-spacing:1.5px;margin-top:10px;text-transform:uppercase}

/* about */
.section-title{position:absolute;left:0;width:1200px;text-align:center;font-size:34px;font-weight:500;text-transform:uppercase}
.section-title::after{content:"";display:block;width:60px;height:3px;background:var(--red);margin:14px auto 0}
.about-title{top:785px;color:var(--blue)}
.about-video{position:absolute;left:88px;top:882px;width:468px;height:259px;
  background:
    radial-gradient(ellipse 170px 110px at 330px 150px,rgba(235,238,242,.75),rgba(235,238,242,0) 80%),
    radial-gradient(ellipse 200px 60px at 140px 175px,rgba(210,214,220,.45),rgba(210,214,220,0) 80%),
    linear-gradient(180deg,#6f7e8f 0%,#566270 50%,#33393f 100%);border:4px solid #8a8a8a}
.play-btn{position:absolute;left:196px;top:95px;width:76px;height:56px;border:4px solid var(--white);border-radius:10px;background:rgba(0,0,0,.25)}
.play-btn::after{content:"";position:absolute;left:26px;top:11px;border-left:24px solid var(--white);border-top:14px solid transparent;border-bottom:14px solid transparent}
.about-copy{position:absolute;left:631px;top:884px;width:473px;font-size:12.5px;line-height:23px;color:#666;font-weight:300}
.about-copy em{color:var(--red);font-style:italic}
.btn-red{position:absolute;left:631px;top:1075px;width:264px;height:64px;background:var(--red);color:var(--white);font-size:15px;font-weight:500;display:flex;align-items:center;justify-content:center;gap:18px;box-shadow:0 4px 0 var(--red-dark);text-transform:uppercase}
.ring-arrow{width:30px;height:30px;border:2px solid var(--white);border-radius:50%;display:flex;align-items:center;justify-content:center}

/* services */
.services{position:absolute;left:0;top:1223px;width:1200px;height:736px;
  background:
    linear-gradient(180deg,rgba(240,74,81,.9),rgba(240,74,81,.88)),
    radial-gradient(ellipse 420px 300px at 900px 380px,#f4f4f4,rgba(244,244,244,0) 80%),
    linear-gradient(180deg,#8fb6dc 0%,#d7c6b0 55%,#6d6d6d 100%)}
.services-title{top:88px;color:var(--white)}
.service-tile{position:absolute;width:324px;height:191px;border:4px solid var(--red-dark);overflow:hidden}
.tile-road{background:
    radial-gradient(ellipse 70px 75px at 125px 100px,rgba(240,240,240,.95),rgba(240,240,240,0) 85%),
    linear-gradient(180deg,#9cc0e2 0%,#cfd9d2 38%,#7d8a5a 58%,#6d7447 74%,#555 100%)}
.tile-trailer{background:
    radial-gradient(ellipse 140px 55px at 110px 105px,rgba(250,250,250,.95),rgba(250,250,250,0) 85%),
    radial-gradient(ellipse 40px 35px at 255px 105px,rgba(200,40,40,.7),rgba(200,40,40,0) 85%),
    linear-gradient(180deg,#2f5fb4 0%,#7ea4d8 42%,#e3e3e3 60%,#8a8072 100%)}
.tile-dusk{background:
    radial-gradient(ellipse 70px 60px at 160px 115px,rgba(90,90,90,.9),rgba(90,90,90,0) 85%),
    linear-gradient(180deg,#6a8fb8 0%,#c9b48a 50%,#5b5b5b 100%)}
.tile-tanker{background:
    radial-gradient(ellipse 95px 50px at 175px 85px,rgba(230,232,236,.95),rgba(230,232,236,0) 85%),
    linear-gradient(180deg,#4f8cd0 0%,#b5c8dc 30%,#d7bd88 52%,#5b5b5b 100%)}
.tile-overlay{position:absolute;inset:0;background:rgba(0,0,0,.55);display:flex;flex-direction:column;align-items:center;justify-content:center;color:var(--white)}
.tile-overlay h3{font-size:20px;font-weight:700;text-transform:uppercase}
.tile-overlay span{margin-top:12px;border:2px solid var(--white);padding:6px 14px;font-size:13px;font-weight:500;text-transform:uppercase}
.btn-white{position:absolute;left:445px;top:616px;width:314px;height:63px;background:var(--white);color:var(--red);font-size:19px;font-weight:500;display:flex;align-items:center;justify-content:center;border-radius:4px;text-transform:uppercase}

/* quote bar */
.quote-bar{position:absolute;left:0;top:1959px;width:1200px;height:159px;background:var(--charcoal);color:var(--white)}
.quote-bar .lead{position:absolute;left:90px;top:52px;font-size:17px;font-style:italic}
.quote-bar h2{position:absolute;left:90px;top:76px;font-size:28px;font-weight:500;text-transform:uppercase}
.btn-quote{position:absolute;left:840px;top:48px;width:272px;height:62px;background:var(--white);color:#222;font-size:23px;font-weight:700;display:flex;align-items:center;justify-content:center;border-radius:4px;text-transform:uppercase}

/* testimonial */
.testimonial{position:absolute;left:0;top:2118px;width:1200px;height:307px;background:var(--blue)}
.quote-card{position:absolute;left:161px;top:56px;width:878px;height:163px;background:var(--white);padding:34px 46px 0 46px;font-size:13px;line-height:24px;font-style:italic;color:#555}
.quote-card::after{content:"";position:absolute;left:44px;bottom:-16px;border-top:16px solid var(--white);border-right:16px solid transparent}
.quote-mark{position:absolute;left:184px;top:24px;width:64px;height:64px;border-radius:50%;background:var(--white);display:flex;align-items:center;justify-content:center}
.quote-author{position:absolute;left:207px;top:253px;font-size:12.5px;color:var(--white);font-weight:500}
.quote-nav{position:absolute;left:990px;top:242px;display:flex;gap:14px}

/* stats */
.stats{position:absolute;left:0;top:2425px;width:1200px;height:310px;
  background:
    radial-gradient(ellipse 170px 140px at 260px 190px,rgba(120,120,120,.55),rgba(120,120,120,0) 85%),
    linear-gradient(100deg,rgba(255,255,255,0) 55%,rgba(255,255,255,.07) 58%,rgba(255,255,255,0) 61%),
    linear-gradient(90deg,#262626 0%,#3a3a3a 40%,#1e1e1e 100%)}
.stat{position:absolute;top:82px;width:192px;color:var(--white)}
.stat strong{display:block;font-size:36px;font-weight:500;padding-bottom:12px;border-bottom:3px solid var(--white);text-transform:uppercase}
.stat span{display:block;margin-top:28px;font-size:22px;line-height:29px;font-weight:300;text-transform:uppercase}

/* footer */
.site-footer{position:absolute;left:0;top:2735px;width:1200px;height:401px;background:var(--red);color:var(--white)}
.footer-brand{position:absolute;left:88px;top:98px;display:flex;align-items:center;gap:14px;font-size:42px;font-weight:700;color:var(--white)}
.footer-brand .brand-dot{width:38px;height:38px;background:var(--white)}
.social{position:absolute;left:88px;top:234px;display:flex;gap:9px}
.social span{width:50px;height:50px;border-radius:50%;background:var(--white);display:flex;align-items:center;justify-content:center}
.footer-links{position:absolute;left:514px;top:92px;width:197px;list-style:none}
.footer-links li{height:38.7px;display:flex;align-items:center;gap:16px;font-size:11px;text-transform:uppercase;border-bottom:1px solid rgba(255,255,255,.3)}
.footer-links li::before{content:"";width:9px;height:9px;background:var(--white)}
.footer-contact{position:absolute;left:817px;top:86px;width:300px}
.footer-contact h4{font-size:15px;font-weight:700;text-transform:uppercase}
.contact-item{position:absolute;display:flex;gap:10px;font-size:11px;line-height:15px}
.newsletter-title{position:absolute;left:817px;top:272px;font-size:15px;font-weight:700;text-transform:uppercase}
.newsletter{position:absolute;left:817px;top:298px;width:295px;height:38px;background:var(--red-dark);display:flex;align-items:center;font-size:11px}
.newsletter .field{flex:1;padding-left:18px;color:rgba(255,255,255,.7)}
.newsletter .send{width:68px;text-align:center;font-weight:700;text-transform:uppercase}
</style>
</head>
<body>

<header class="site-header">
  <div class="brand"><span class="brand-dot"></span>Heron Freightways</div>
  <nav class="main-nav">
    <a class="active">Home</a><a>Services</a><a>Why Us</a><a>Careers</a><a>About Us</a><a>Contact Us</a>
  </nav>
</header>

<section class="hero" role="img" aria-label="Yellow semi truck with white trailer on a desert highway under blue sky">
  <div class="hero-arrow prev"><svg width="18" height="28" viewBox="0 0 18 28"><path d="M14 3 4 14l10 11" fill="none" stroke="#fff" stroke-width="4"/></svg></div>
  <div class="hero-caption">
    <h1>Largest Freight<br>Network in South Texas</h1>
    <p>Road, air, train or overseas. We got it covered!</p>
  </div>
  <div class="hero-arrow next"><svg width="18" height="28" viewBox="0 0 18 28"><path d="M4 3l10 11L4 25" fill="none" stroke="#fff" stroke-width="4"/></svg></div>
</section>

<h2 class="section-title about-title">About Us</h2>
<div class="about-video" role="img" aria-label="Video still of a line of parked white trucks"><span class="play-btn"></span></div>
<p class="about-copy">We carry and deliver almost any type of temperature sensitive products anywhere in the United States.<br>Heron Freightways, LLC currently has the very latest in transport refrigeration technology. Our brand new trucks and professional looking equipment set the standard with outstanding efficiency and reliability paired with superior temperature control.<br>We offer quality and reliability. We've got you and your business covered day and night, from origin to destination. <em>More</em></p>
<div class="btn-red">Browse More Videos <span class="ring-arrow"><svg width="12" height="12" viewBox="0 0 12 12"><path d="M1 6h9M6 2l4 4-4 4" fill="none" stroke="#fff" stroke-width="2"/></svg></span></div>

<section class="services" role="img" aria-label="Faint truck photo behind a red overlay">
  <h2 class="section-title services-title">What Excatly We Do</h2>
  <div class="service-tile tile-road" style="left:88px;top:169px" role="img" aria-label="Road train truck on a country highway"></div>
  <div class="service-tile tile-dusk" style="left:441px;top:169px" role="img" aria-label="Truck on a road at dusk"><div class="tile-overlay"><h3>Dedicated Service</h3><span>Learn More</span></div></div>
  <div class="service-tile tile-trailer" style="left:788px;top:169px" role="img" aria-label="White trailer truck on a highway"></div>
  <div class="service-tile tile-road" style="left:88px;top:384px" role="img" aria-label="Road train truck on a country highway"></div>
  <div class="service-tile tile-tanker" style="left:441px;top:384px" role="img" aria-label="Chrome tanker truck on a highway"></div>
  <div class="service-tile tile-trailer" style="left:788px;top:384px" role="img" aria-label="White trailer truck on a highway"></div>
  <div class="btn-white">Browse All Services</div>
</section>

<section class="quote-bar">
  <p class="lead">Facing any transpoortation problem?</p>
  <h2>Connect with our experts and get relaxed!</h2>
  <div class="btn-quote">Get a Quote</div>
</section>

<section class="testimonial">
  <div class="quote-card">Lorem ipsum dolor sit amet, consectetur adipiscing elit, sed do eiusmod tempor incididunt ut labore et dolore magna aliqua. Ut enim ad minim veniam, quis nostrud exercitation ullamco laboris nisi ut aliquip ex ea commodo consequat. Duis aute irure dolor in reprehenderit in voluptate velit esse cillum dolore eu fugiat nulla pariatur. Excepteur sint occaecat cupidatat non proident, sunt in culpa qui officia deserunt mollit anim id est laborum</div>
  <div class="quote-mark"><svg width="26" height="20" viewBox="0 0 26 20"><path d="M0 20V11C0 4 4 1 10 0v4c-3 1-5 3-5 6h5v10zM15 20V11c0-7 4-10 10-11v4c-3 1-5 3-5 6h5v10z" fill="#222"/></svg></div>
  <div class="quote-author">Marisol Vandeker</div>
  <div class="quote-nav">
    <svg width="14" height="20" viewBox="0 0 14 20"><path d="M11 2 3 10l8 8" fill="none" stroke="#fff" stroke-width="3"/></svg>
    <svg width="14" height="20" viewBox="0 0 14 20"><path d="M3 2l8 8-8 8" fill="none" stroke="#fff" stroke-width="3"/></svg>
  </div>
</section>

<section class="stats" role="img" aria-label="Dark photo of a truck on a multi-lane highway">
  <div class="stat" style="left:119px"><strong>35 Years</strong><span>Of transportation experience</span></div>
  <div class="stat" style="left:376px"><strong>22 +</strong><span>Trsnaportation facilities provided</span></div>
  <div class="stat" style="left:631px"><strong>6,959 +</strong><span>Satisfied customers around globe</span></div>
  <div class="stat" style="left:888px"><strong>22,258</strong><span>Highly skilled drivers in our fleet</span></div>
</section>

<footer class="site-footer">
  <div class="footer-brand"><span class="brand-dot"></span>Heron Freightways</div>
  <div class="social">
    <span aria-label="Share"><svg width="22" height="22" viewBox="0 0 24 24"><circle cx="18" cy="5" r="3" fill="#f04a51"/><circle cx="6" cy="12" r="3" fill="#f04a51"/><circle cx="18" cy="19" r="3" fill="#f04a51"/><path d="M8.5 10.5l7-4M8.5 13.5l7 4" stroke="#f04a51" stroke-width="2"/></svg></span>
    <span aria-label="Chat"><svg width="22" height="22" viewBox="0 0 24 24"><path d="M3 4h18v12H9l-5 4v-4H3z" fill="#f04a51"/></svg></span>
    <span aria-label="Website"><svg width="22" height="22" viewBox="0 0 24 24"><circle cx="12" cy="12" r="9" fill="none" stroke="#f04a51" stroke-width="2"/><ellipse cx="12" cy="12" rx="4" ry="9" fill="none" stroke="#f04a51" stroke-width="2"/><path d="M3 12h18" stroke="#f04a51" stroke-width="2"/></svg></span>
  </div>
  <ul class="footer-links">
    <li>Contact Us</li><li>FAQ.s</li><li>Careers</li><li>Our Branches</li><li>Customer Care</li><li>Partners</li><li>Collaborations</li>
  </ul>
  <div class="footer-contact">
    <h4>Contact Us</h4>
    <div class="contact-item" style="left:0;top:40px">
      <svg width="16" height="22" viewBox="0 0 16 22"><path d="M8 0a8 8 0 0 0-8 8c0 6 8 14 8 14s8-8 8-14a8 8 0 0 0-8-8z" fill="#fff"/><circle cx="8" cy="8" r="3" fill="#f04a51"/></svg>
      <span>Main Office:<br>4180 W. Palmera Ave.<br>Alton, TX 78599</span>
    </div>
    <div class="contact-item" style="left:0;top:112px">
      <svg width="18" height="13" viewBox="0 0 18 13"><rect width="18" height="13" fill="#fff"/><path d="M0 0l9 7 9-7" fill="none" stroke="#f04a51" stroke-width="1.5"/></svg>
      <span>info@heronfreightways.net</span>
    </div>
    <div class="contact-item" style="left:172px;top:42px">
      <svg width="18" height="18" viewBox="0 0 24 24"><path d="M6.6 10.8a15 15 0 0 0 6.6 6.6l2.2-2.2a1 1 0 0 1 1-.3 11 11 0 0 0 3.6.6 1 1 0 0 1 1 1V20a1 1 0 0 1-1 1A17 17 0 0 1 3 4a1 1 0 0 1 1-1h3.5a1 1 0 0 1 1 1 11 11 0 0 0 .6 3.6 1 1 0 0 1-.3 1z" fill="#fff"/></svg>
      <span>Toll Free Number<br>1-800-555-0142</span>
    </div>
    <div class="contact-item" style="left:172px;top:104px">
      <svg width="18" height="18" viewBox="0 0 24 24"><path d="M6.6 10.8a15 15 0 0 0 6.6 6.6l2.2-2.2a1 1 0 0 1 1-.3 11 11 0 0 0 3.6.6 1 1 0 0 1 1 1V20a1 1 0 0 1-1 1A17 17 0 0 1 3 4a1 1 0 0 1 1-1h3.5a1 1 0 0 1 1 1 11 11 0 0 0 .6 3.6 1 1 0 0 1-.3 1z" fill="#fff"/></svg>
      <span>Local Number<br>(956) 555-0187</span>
    </div>
  </div>
  <div class="newsletter-title">Subscribe to our newsletter</div>
  <div class="newsletter"><span class="field">Enter your email address</span><span class="send">Send</span></div>
</footer>

</body>
</html>
```